Health and Wellness Company Needs Brochure to Describe New Exercise Class Offering

We need a brochure to help clients better understand our new service offering. We are a Portland, OR based health and wellness company called 'north stride studio'. We provide instruction in group exercise classes designed to reduce pain and improve movement. Similar to physical therapy but with the teaching environment similar to a yoga studio.

Please see attached word document that outlines the sections that should be included in the brochure.

We would like to see the color orange throughout the brochure as that color reflects vitality and energy. Our logo should be included in the design. Our slogan is "Feel Better. Move Better. Live Better." Go to our website www.northstridestudio.example for more information.

Target Market(s)

Exercise conscious, recreational athletes who are proactive about their health and well-being and looking for an alternative to physical therapy.

Industry/Entity Type

Health And Wellness

Font styles to use
Sans Serif

Requirements
Must have
• Logo placed strategically throughout the brochure.
• A trifold brochure.
Should not have
• I'd like to avoid the standard 3 panel design. Instead I'd like to see the design spread out over the page with 3 sections arbitrarily created by the designer that doesn't follow the fold pattern of the trifold brochure.

```html
<!DOCTYPE html>
<html lang="en">
<head>
<meta charset="utf-8">
<title>north stride studio – trifold brochure</title>
<link href="https://fonts.googleapis.com/css2?family=Lato:wght@400;700&family=Oswald:wght@400;500&display=swap" rel="stylesheet">
<style>
  :root {
    --page-bg: #e9e9ec;
    --paper: #ffffff;
    --violet: #4b52a3;
    --orange: #f5820a;
    --orange-soft: #f79a32;
    --grey-band: #a9aaad;
    --ink: #1d1d1f;
    --body-ink: #2a2a2a;
    --photo-skin: #d8b49a;
    --photo-road: #5c5a66;
    --photo-studio: #f1ebe6;
  }
  html, body {
    margin: 0;
    width: 1200px;
    height: 1200px;
    overflow: hidden;
    background: var(--page-bg);
  }
  .brochure-spread {
    position: absolute;
    left: 0;
    top: 172px;
    width: 1200px;
    height: 855px;
    display: block;
  }
  .headline-what { font-family: "Lato", sans-serif; font-weight: 700; font-size: 25px; fill: #fff; }
  .headline-sub { font-family: "Lato", sans-serif; font-weight: 400; font-size: 17.5px; fill: #fff; }
  .headline-accent { fill: var(--orange); }
  .body-copy { font-family: "Lato", sans-serif; font-size: 7.6px; fill: #fff; }
  .wordmark { font-family: "Lato", sans-serif; font-weight: 700; font-size: 15px; }
  .wordmark-light { fill: #fff; }
  .wordmark-violet { fill: var(--violet); }
  .coupon-lead { font-family: "Lato", sans-serif; font-size: 16px; fill: var(--violet); }
  .coupon-offer { font-family: "Oswald", sans-serif; font-size: 14px; fill: var(--orange); }
  .coupon-copy { font-family: "Lato", sans-serif; font-size: 8.6px; fill: var(--body-ink); }
  .coupon-free { fill: var(--orange); font-weight: 700; }
  .reserve-line { font-family: "Oswald", sans-serif; font-size: 13px; fill: var(--violet); }
  .web-line { font-family: "Oswald", sans-serif; font-size: 13px; fill: var(--orange); }
  .cover-word { font-family: "Oswald", sans-serif; font-weight: 500; }
  .cover-exercise { font-size: 32px; fill: var(--violet); }
  .cover-pain { font-size: 46px; fill: var(--ink); }
  .cover-move { font-size: 44px; fill: #fff; }
</style>
</head>
<body>
<svg class="brochure-spread" viewBox="0 0 828 590" xmlns="http://www.w3.org/2000/svg" aria-label="north stride studio trifold brochure, outside spread">
  <defs>
    <linearGradient id="fold-shade-mid" x1="0" x2="1" y1="0" y2="0">
      <stop offset="0" stop-color="#000" stop-opacity="0.10"/>
      <stop offset="0.25" stop-color="#000" stop-opacity="0"/>
    </linearGradient>
    <linearGradient id="fold-shade-right" x1="0" x2="1" y1="0" y2="0">
      <stop offset="0" stop-color="#000" stop-opacity="0.06"/>
      <stop offset="0.2" stop-color="#000" stop-opacity="0"/>
    </linearGradient>
    <linearGradient id="mirror-photo" x1="0" x2="1" y1="0" y2="1">
      <stop offset="0" stop-color="#f4eee9"/>
      <stop offset="0.5" stop-color="var(--photo-skin)"/>
      <stop offset="1" stop-color="#e9e3de"/>
    </linearGradient>
    <linearGradient id="studio-photo" x1="0" x2="0" y1="0" y2="1">
      <stop offset="0" stop-color="#faf7f4"/>
      <stop offset="0.6" stop-color="#ecd9cc"/>
      <stop offset="1" stop-color="#d9685c"/>
    </linearGradient>
    <linearGradient id="road-photo" x1="0" x2="0" y1="0" y2="1">
      <stop offset="0" stop-color="#9fa37a"/>
      <stop offset="0.3" stop-color="#c2523f"/>
      <stop offset="0.6" stop-color="var(--photo-road)"/>
      <stop offset="1" stop-color="#3f3d47"/>
    </linearGradient>
  </defs>

  <rect class="paper" x="0" y="0" width="828" height="590" fill="var(--paper)"/>

  <g class="panel panel-posture">
    <polygon class="band-grey" points="0,0 281,0 281,28 0,14" fill="var(--grey-band)"/>
    <polygon class="shape-violet" points="0,14 120,36 281,95 281,120 0,300" fill="var(--violet)"/>
    <polygon class="shape-orange" points="281,120 281,362 0,415 0,300" fill="var(--orange)"/>
    <polygon class="strip-violet" points="0,415 281,362 281,386 0,420" fill="var(--violet)"/>
    <polygon class="photo-mirror" role="img" aria-label="Photo: woman checking her posture in a mirror"
             points="0,420 281,386 281,590 0,590" fill="url(#mirror-photo)"/>

    <text class="headline-what" x="23" y="107">What</text>
    <text class="headline-sub" x="23" y="131">Does Your <tspan class="headline-accent">POSTURE</tspan></text>
    <text class="headline-sub" x="23" y="154">Say About You?</text>

    <g class="body-copy" text-anchor="end">
      <text x="248" y="207">The</text>
      <text x="248" y="218">easiest</text>
      <text x="248" y="230">way to identify</text>
      <text x="248" y="241">muscle compensation</text>
      <text x="248" y="253">is to look for misalignments</text>
      <text x="248" y="264">in your body.  Place your hands on</text>
      <text x="248" y="276">your waist line.  Is one hip higher than</text>
      <text x="248" y="287">the other? Does one foot turn out more?  Is</text>
      <text x="248" y="298">one shoulder higher than the other?</text>
      <text x="248" y="321">If you answered YES to any of these questions, your</text>
      <text x="248" y="332">pain is likely the result of muscle compensation and can</text>
      <text x="248" y="343">benefit from the north stride method!</text>
    </g>
  </g>

  <polygon class="band-grey band-main" points="281,0 281,15 828,200 828,292 555,195 281,100" fill="var(--grey-band)"/>
  <polygon class="band-orange band-exercise" points="610,120 828,52 828,168 720,165" fill="var(--orange)"/>
  <polygon class="band-orange band-move-fold" points="468,272 495,176 555,196 555,302" fill="var(--orange-soft)"/>
  <polygon class="band-orange band-move" points="555,196 828,292 828,385 555,302" fill="var(--orange)"/>

  <g class="panel panel-coupon">
    <rect x="281" y="0" width="274" height="590" fill="url(#fold-shade-mid)"/>
    <text class="wordmark wordmark-light" x="377" y="105" text-anchor="middle">north stride studio</text>

    <text class="coupon-lead" x="373" y="180" text-anchor="middle">A coupon for</text>
    <text class="coupon-offer" x="373" y="201" text-anchor="middle">“FREE INTRODUCTORY CLASS”</text>
    <g class="coupon-copy" text-anchor="middle">
      <text x="373" y="220">To learn more about how to</text>
      <text x="373" y="232">restore balance in your body, and for</text>
      <text x="373" y="244">a <tspan class="coupon-free">FREE</tspan> posture assessment, sign up</text>
      <text x="373" y="256">for our <tspan class="coupon-free">FREE</tspan> Introductory Class.</text>
    </g>
    <text class="reserve-line" x="373" y="284" text-anchor="middle">Reserve your space online at</text>
    <text class="web-line" x="373" y="302" text-anchor="middle">www.northstridestudio.example</text>

    <rect class="photo-yoga" role="img" aria-label="Photo: woman in a seated yoga twist on a mat"
          x="300" y="338" width="236" height="252" fill="url(#studio-photo)"/>
  </g>

  <g class="panel panel-cover">
    <rect x="555" y="0" width="273" height="590" fill="url(#fold-shade-right)"/>
    <rect class="wordmark-mark" x="618" y="38" width="12" height="12" fill="var(--violet)"/>
    <text class="wordmark wordmark-violet" x="643" y="70" text-anchor="middle">north stride studio</text>

    <polygon class="photo-runner" role="img" aria-label="Photo: runner stretching a sore leg on a country road"
             points="555,302 828,385 828,590 555,590" fill="url(#road-photo)"/>

    <text class="cover-word cover-exercise" x="752" y="128" text-anchor="middle" transform="rotate(-17 752 128)">EXERCISE</text>
    <text class="cover-word cover-pain" x="695" y="225" text-anchor="middle" transform="rotate(17 695 225)">PAIN AWAY</text>
    <text class="cover-word cover-move" x="692" y="312" text-anchor="middle" transform="rotate(17 692 312)">MOVE EASIER</text>
  </g>
</svg>
</body>
</html>
```